4R Capital business cards for a tech VC

We're starting a new Venture Capital that is focusing on bringing the best start ups from Israel to NYC
We need a business cards template for this that gives the sense of an entrepreneurial look
I don't want any religious signs on this even thought it's Israel
I'm looking for a techi feeling but not too crazy
The card should probably be in the same light blue as the logo and the logo in white

Target Market(s)

Investors

Industry/Entity Type

Tech

Contact Information for Business Card

The card needs to look slick and entrepreneurship like
The VC is focused on NYC and Tel Aviv so could be great to show something on the back side that is like NYC skyline or something like that
You can see the logo attached

Colors
0455a3
3276b5
85acd3
cedeed
eaf1f7

Requirements
Must have
• A very cool looking business card that shows we're a cutting edge tech VC with a focus on bringing start ups from Tel Aviv and leveraging the NYC ecosystem
Nice to have
• NYC skyline can be cool , maybe something that is connected to Tel Aviv

```html
<!DOCTYPE html>
<html lang="en">
<head>
<meta charset="utf-8">
<title>4R Capital – Business Cards</title>
<link href="https://fonts.googleapis.com/css2?family=Open+Sans:wght@400;600;700&display=swap" rel="stylesheet">
<style>
  :root {
    --brand-blue: #1b6a98;
    --brand-blue-deep: #145a83;
    --ink: #1d1d1f;
    --paper: #ffffff;
    --backdrop: #e8ebee;
    --skyline-soft: #85acd3;
  }
  * { box-sizing: border-box; margin: 0; padding: 0; }
  html, body {
    width: 1200px;
    height: 1021px;
    overflow: hidden;
    background: var(--backdrop);
    font-family: "Open Sans", Arial, sans-serif;
  }
  .sheet {
    position: relative;
    width: 1200px;
    height: 1021px;
  }
  .card {
    position: absolute;
    left: 250px;
    width: 700px;
    height: 400px;
    border-radius: 4px;
    box-shadow: 0 6px 18px rgba(0,0,0,0.12);
    overflow: hidden;
  }

  /* Front */
  .card-front {
    top: 80px;
    background: var(--paper);
  }
  .identity {
    position: absolute;
    left: 44px;
    top: 150px;
    padding-left: 20px;
    border-left: 10px solid var(--brand-blue);
  }
  .identity-name {
    font-size: 30px;
    line-height: 1.05;
    color: var(--ink);
    font-weight: 400;
  }
  .identity-name strong { font-weight: 700; }
  .identity-title {
    font-size: 18px;
    color: var(--brand-blue);
    margin-top: 2px;
  }
  .brand-front {
    position: absolute;
    right: 56px;
    top: 56px;
    display: flex;
    align-items: center;
    gap: 14px;
  }
  .brand-mark {
    width: 22px;
    height: 22px;
    background: var(--brand-blue);
  }
  .brand-name {
    font-size: 42px;
    font-weight: 700;
    color: var(--brand-blue);
    letter-spacing: 1px;
  }
  .contact-list {
    position: absolute;
    left: 64px;
    bottom: 44px;
    list-style: none;
  }
  .contact-item {
    display: flex;
    align-items: center;
    gap: 14px;
    font-size: 17px;
    color: var(--ink);
    margin-top: 10px;
  }
  .contact-icon { width: 18px; height: 18px; flex: none; }

  /* Back */
  .card-back {
    top: 541px;
    background: var(--brand-blue);
  }
  .brand-back {
    position: absolute;
    left: 0;
    right: 0;
    top: 70px;
    display: flex;
    justify-content: center;
    align-items: center;
    gap: 14px;
  }
  .brand-back .brand-mark { background: var(--paper); }
  .brand-back .brand-name { color: var(--paper); font-size: 48px; }
  .tagline {
    position: absolute;
    left: 50%;
    top: 172px;
    transform: translateX(-50%);
    white-space: nowrap;
    border: 2px solid var(--paper);
    color: var(--paper);
    font-size: 15px;
    letter-spacing: 0.6px;
    padding: 6px 16px;
  }
  .skyline {
    position: absolute;
    left: 0;
    right: 0;
    bottom: 0;
    height: 130px;
    background: linear-gradient(to top, rgba(20,90,131,0.9), rgba(133,172,211,0.12) 65%, rgba(133,172,211,0));
  }
</style>
</head>
<body>
<main class="sheet">

  <section class="card card-front" aria-label="Business card front">
    <div class="brand-front">
      <span class="brand-mark"></span>
      <span class="brand-name">4R Capital</span>
    </div>

    <div class="identity">
      <p class="identity-name">Your <strong>Name</strong></p>
      <p class="identity-title">Job Title</p>
    </div>

    <ul class="contact-list">
      <li class="contact-item">
        <svg class="contact-icon" viewBox="0 0 24 24" aria-hidden="true">
          <path fill="#1b6a98" d="M6.6 10.8a15 15 0 0 0 6.6 6.6l2.2-2.2a1 1 0 0 1 1-.25 11.4 11.4 0 0 0 3.6.57 1 1 0 0 1 1 1V20a1 1 0 0 1-1 1A17 17 0 0 1 3 4a1 1 0 0 1 1-1h3.5a1 1 0 0 1 1 1c0 1.250.2 2.450.57 3.570a1 1 0 0 1-.25 1z"/>
        </svg>
        <span>000 000 0000</span>
      </li>
      <li class="contact-item">
        <svg class="contact-icon" viewBox="0 0 24 24" aria-hidden="true">
          <rect x="2" y="5" width="20" height="14" rx="1.5" fill="#1b6a98"/>
          <path d="M3 6l9 7 9-7" fill="none" stroke="#fff" stroke-width="1.6"/>
        </svg>
        <span>email@xyz.com</span>
      </li>
      <li class="contact-item">
        <svg class="contact-icon" viewBox="0 0 24 24" aria-hidden="true">
          <g fill="none" stroke="#1b6a98" stroke-width="1.8">
            <circle cx="12" cy="12" r="9.5"/>
            <ellipse cx="12" cy="12" rx="4.2" ry="9.5"/>
            <path d="M2.5 12h19M4 7h16M4 17h16"/>
          </g>
        </svg>
        <span>yourwebsite.com</span>
      </li>
    </ul>
  </section>

  <section class="card card-back" aria-label="Business card back">
    <div class="brand-back">
      <span class="brand-mark"></span>
      <span class="brand-name">4R Capital</span>
    </div>
    <p class="tagline">Backing Bold Founders From Tel Aviv. Scaling Them Through New York.</p>
    <div class="skyline" role="img" aria-label="Thin line drawing of a city skyline with a harbour statue along the bottom edge"></div>
  </section>

</main>
</body>
</html>
```